PowerPoint Template Design for business consulting company in Silicon Valley

I need a PowerPoint template to use as the starting point for new presentations. I have a logo but now need design that supports this. I've attached a very descriptive PDF that explains exactly what I need. Here is a list of deliverables: 1. PowerPoint Template that I will use as the starter presentation for all new Vantor Bellway presentationsDesigns for the following slides: See picture below for examples of structure:2. Title slide with subtitle3. Section header4. Title and body5. Title and 2 columns6. Title and 3 columns7. One column text8. Editable timeline to show months, or steps for a process9. Bullet design for unordered list (can be graphic)10. Bullet design for ordered list11. Recommended fonts for each design: Title, subtitle, list, captionOPTIONAL: Possible graphic elements to be used for section title slide backgrounds or graphic elements:--Your team / my team / people on project--Goals for project / presentation--Editable Timeline--Speaking--Writing--Listening--People collaborating / helping each otherI am happy to accept proposals for developing these optional elements in a separate project.

Requirements
Must have
• Must be FLAT design.
• Not flashy or garish. Must be subtle.

```html
<!DOCTYPE html>
<html lang="en">
<head>
<meta charset="utf-8">
<title>Vantor Bellway — Presentation Template</title>
<link href="https://fonts.googleapis.com/css2?family=Alegreya:wght@500;700&family=Open+Sans:wght@400;600&display=swap" rel="stylesheet">
<style>
  :root{
    --blue:#22409a;
    --green:#1c7a35;
    --grey-icon:#c9cdd0;
    --text:#6a6a6a;
    --num:#dfe7e2;
    --paper:#eeeae3;
    --canvas:#f2f2f2;
    --white:#ffffff;
    --panel:#f3f4f3;
  }
  *{box-sizing:border-box;margin:0;padding:0}
  html,body{width:1200px;height:2458px;overflow:hidden;background:var(--canvas)}
  .sheet{
    width:1200px;height:2458px;padding:5px 9px;
    display:grid;grid-template-columns:repeat(3,386px);grid-template-rows:repeat(11,218px);
    column-gap:12px;row-gap:5px;
  }
  .slide{position:relative;overflow:hidden;background:var(--white);font-family:"Open Sans",sans-serif;color:var(--text);box-shadow:0 0 2px rgba(0,0,0,.12)}
  .slide.paper{background:var(--paper)}
  .slide.fill-blue{background:var(--blue)}
  .slide.fill-green{background:var(--green)}
  .head{position:absolute;left:18px;top:13px;font-family:"Alegreya",serif;font-weight:500;font-size:15px;color:var(--blue)}
  .mark{position:absolute;right:8px;top:8px;display:flex;align-items:center;gap:3px;font-family:"Alegreya",serif;font-weight:500;font-size:8px;color:var(--green);line-height:1}
  .mark .ring{width:14px;height:14px;border-radius:50%;border:1.5px solid var(--green)}
  .mark.left{left:14px;right:auto;top:14px;font-size:10px}
  .mark.left .ring{width:18px;height:18px}
  .num{position:absolute;right:10px;bottom:-8px;font-family:"Alegreya",serif;font-weight:500;font-size:46px;color:var(--num);line-height:1}
  .circuit{position:absolute}
  .photo{position:absolute}
  .copy{font-size:6.3px;line-height:1.4;color:var(--text)}
  .serif{font-family:"Alegreya",serif}
  /* vertical timeline */
  .vline{position:absolute;left:200px;top:30px;width:1px;bottom:0;background:#d4d4d4}
  .vnode{position:absolute;width:26px;height:26px;border-radius:50%;display:flex;align-items:center;justify-content:center}
  .vnode::after{content:"";width:10px;height:10px;border-radius:50%;border:1.5px solid var(--white)}
  .is-green{background:var(--green)} .is-blue{background:var(--blue)} .is-grey{background:var(--grey-icon)}
  .vlabel{position:absolute;width:110px}
  .vlabel b{display:block;font-family:"Alegreya",serif;font-weight:500;font-size:8.5px;color:var(--green)}
  .vlabel span{display:block;font-size:5.5px;line-height:1.35}
  .vlabel.to-left{text-align:right}
  /* horizontal timeline */
  .hline{position:absolute;left:14px;right:14px;top:104px;height:1px;background:#d4d4d4}
  .hnode{position:absolute;width:26px;height:26px;border-radius:50%;display:flex;align-items:center;justify-content:center;transform:translateX(-50%)}
  .hnode::after{content:"";width:10px;height:10px;border-radius:50%;border:1.5px solid var(--white)}
  .hnode.up{top:76px} .hnode.down{top:120px}
  .htick{position:absolute;top:101px;width:6px;height:6px;border-radius:50%;background:var(--blue);transform:translateX(-50%)}
  .hlabel{position:absolute;font-family:"Alegreya",serif;font-weight:500;font-size:8.5px;color:var(--green);transform:translateX(-50%);white-space:nowrap}
  .hlabel.up{top:60px} .hlabel.down{top:150px;color:var(--blue)}
  /* big words */
  .word{position:absolute;left:0;right:0;top:50%;transform:translateY(-50%);text-align:center;font-family:"Alegreya",serif;font-weight:700;font-size:48px;line-height:1.05}
  .phrase{position:absolute;left:22px;top:34px;font-family:"Alegreya",serif;font-weight:500;font-size:32px;line-height:1.18;color:var(--white)}
  .big-number{font-family:"Alegreya",serif;font-weight:700;color:var(--blue);line-height:1}
  .big-caption{font-family:"Alegreya",serif;font-weight:500;color:var(--green)}
  /* lists */
  .bullets{list-style:none}
  .bullets li{position:relative;padding-left:12px}
  .bullets li::before{content:"";position:absolute;left:0;top:.35em;width:6px;height:6px;border-radius:50%;border:1.5px solid var(--green)}
  .col-panel{position:absolute;background:var(--panel);padding:6px 7px}
  .pin{position:absolute;transform:translate(-50%,-100%);display:flex;flex-direction:column;align-items:center}
  .pin i{width:30px;height:30px;border-radius:50%;display:flex;align-items:center;justify-content:center;font-style:normal;font-size:8px;font-weight:600;color:var(--white)}
  .pin::after{content:"";width:1.5px;height:16px;background:currentColor}
  .person-ico{display:inline-block;width:5px;height:10px;border-radius:2px;margin-right:1.5px}
  .member{position:absolute;display:flex;gap:8px;width:160px}
  .avatar{flex:none;width:38px;height:38px;border-radius:50%;background:linear-gradient(160deg,#b9a795,#6f6a66)}
  .member b{display:block;font-size:7px;color:#444}
  .member em{display:block;font-style:normal;font-size:5.5px;color:var(--green)}
  .member span{display:block;font-size:5px;line-height:1.4}
  .card{position:absolute;top:66px;width:58px;height:106px;border:1.5px solid var(--blue);border-radius:8px 8px 0 8px;overflow:hidden}
  .card .tab{height:34px;display:flex;align-items:center;justify-content:center}
  .card .tab::after{content:"";width:12px;height:12px;border-radius:3px;border:1.5px solid var(--white)}
  .card .lbl{position:absolute;left:4px;right:4px;bottom:10px;height:18px;border:1px solid var(--blue);border-radius:4px;display:flex;align-items:center;justify-content:center;font-size:5.5px;font-weight:600;color:var(--blue)}
</style>
</head>
<body>
<main class="sheet">

  <!-- 1 Title -->
  <section class="slide paper">
    <div class="circuit" role="img" aria-label="Blue circuit-line decoration" style="left:0;top:0;width:230px;height:74px;background:linear-gradient(90deg,rgba(34,64,154,.35),rgba(34,64,154,.05))"></div>
    <h1 class="serif" style="position:absolute;right:18px;top:132px;font-weight:700;font-size:23px;color:var(--blue)">Your Presentation Title Here</h1>
    <p class="serif" style="position:absolute;right:18px;top:160px;font-size:10px;color:var(--blue)">Your Presentation Subtitle Here</p>
  </section>

  <!-- 2 Title alt -->
  <section class="slide">
    <div class="mark left"><span class="ring"></span>Vantor Bellway</div>
    <h1 class="serif" style="position:absolute;left:20px;top:88px;font-weight:700;font-size:21px;color:var(--blue)">Your Presentation Title Here</h1>
    <p class="serif" style="position:absolute;left:20px;top:115px;font-size:9px;color:var(--blue)">Your Presentation Subtitle Here</p>
    <div class="circuit" role="img" aria-label="Blue and green circuit-line decoration" style="right:0;bottom:0;width:160px;height:80px;background:linear-gradient(135deg,rgba(28,122,53,.05),rgba(34,64,154,.35))"></div>
  </section>

  <!-- 3 Section -->
  <section class="slide paper">
    <div class="mark"><span class="ring"></span>Vantor Bellway</div>
    <h2 class="serif" style="position:absolute;left:0;right:0;top:112px;text-align:center;font-weight:700;font-size:21px;color:var(--green)">Your Section Title Here</h2>
    <div class="circuit" role="img" aria-label="Green circuit-line decoration" style="left:0;bottom:0;width:250px;height:62px;background:linear-gradient(90deg,rgba(28,122,53,.4),rgba(28,122,53,.03))"></div>
  </section>

  <!-- 4 Timeline vertical -->
  <section class="slide">
    <h2 class="head">Our Timeline</h2>
    <div class="mark"><span class="ring"></span>Vantor Bellway</div>
    <div class="vline"></div>
    <div class="vnode is-green" style="left:157px;top:92px"></div>
    <div class="vlabel to-left" style="left:42px;top:92px"><b>Opening</b><span>Add a short note about this step here.</span></div>
    <div class="vnode is-blue" style="left:217px;top:136px"></div>
    <div class="vlabel" style="left:252px;top:136px"><b>Introduction</b><span>Add a short note about this step here.</span></div>
    <div class="num">4</div>
  </section>

  <!-- 5 Section alt -->
  <section class="slide">
    <div class="mark left"><span class="ring"></span>Vantor Bellway</div>
    <div class="circuit" role="img" aria-label="Green circuit-line decoration" style="right:0;top:0;width:170px;height:74px;background:linear-gradient(270deg,rgba(28,122,53,.35),rgba(28,122,53,.03))"></div>
    <h2 class="serif" style="position:absolute;left:22px;top:136px;font-weight:700;font-size:19px;color:var(--green)">Your Section Title Here</h2>
  </section>

  <!-- 6 Text area -->
  <section class="slide">
    <h2 class="head">Text Area Goes Here</h2>
    <div class="mark"><span class="ring"></span>Vantor Bellway</div>
    <p style="position:absolute;left:18px;top:40px;width:300px;font-size:7.5px;font-weight:600;line-height:1.4;color:var(--blue)">This is place for your header text. Insert your text here, just replace this text with your own text.</p>
    <p class="copy" style="position:absolute;left:18px;top:66px;width:318px">Lorem ipsum dolor sit amet, consectetur adipiscing elit, sed do eiusmod tempor incididunt ut labore et dolore magna aliqua. Ut enim ad minim veniam, quis nostrud exercitation ullamco laboris nisi ut aliquip ex ea.</p>
    <p class="copy" style="position:absolute;left:18px;top:102px;width:318px">Duis aute irure dolor in reprehenderit in voluptate velit esse cillum dolore eu fugiat nulla pariatur. Excepteur sint occaecat cupidatat non proident, sunt in culpa qui officia deserunt mollit anim id est.</p>
    <div class="num">6</div>
  </section>

  <!-- 7 Timeline continued -->
  <section class="slide">
    <div class="mark"><span class="ring"></span>Vantor Bellway</div>
    <div class="vline" style="top:0"></div>
    <div class="vnode is-grey" style="left:157px;top:22px"></div>
    <div class="vlabel to-left" style="left:42px;top:22px"><b>Our Client</b><span>Add a short note about this step here.</span></div>
    <div class="vnode is-grey" style="left:217px;top:72px"></div>
    <div class="vlabel" style="left:252px;top:72px"><b>Testimonial</b><span>Add a short note about this step here.</span></div>
    <div class="vnode is-green" style="left:157px;top:115px"></div>
    <div class="vlabel to-left" style="left:42px;top:115px"><b>Coffee Break</b><span>Add a short note about this step here.</span></div>
    <div class="vnode is-blue" style="left:217px;top:156px"></div>
    <div class="vlabel" style="left:252px;top:156px"><b>Our Process</b><span>Add a short note about this step here.</span></div>
    <div class="num">7</div>
  </section>

  <!-- 8 Picture and text -->
  <section class="slide">
    <h2 class="head" style="font-size:13px">Picture and Text</h2>
    <div class="mark"><span class="ring"></span>Vantor Bellway</div>
    <div class="photo" role="img" aria-label="Round photo of wooden blocks on a desk" style="left:28px;top:60px;width:98px;height:98px;border-radius:50%;background:radial-gradient(circle at 40% 40%,#f3d3b0,#c98a52 60%,#e9e4de)"></div>
    <p class="serif" style="position:absolute;left:190px;top:72px;font-weight:700;font-size:23px;line-height:1.2;color:var(--blue)">We are<br>Vantor<br>Bellway</p>
  </section>

  <!-- 9 Who we are -->
  <section class="slide">
    <div class="mark"><span class="ring"></span>Vantor Bellway</div>
    <div class="photo" role="img" aria-label="Photo of business people shaking hands in front of a city skyline" style="left:0;top:0;width:192px;height:218px;background:linear-gradient(180deg,#8fb4d8,#d3c1a3 60%,#5e5a6a)"></div>
    <p class="serif" style="position:absolute;left:12px;top:166px;font-weight:700;font-size:19px;color:var(--white)">Who We Are</p>
    <p class="serif" style="position:absolute;left:212px;top:58px;width:160px;font-weight:700;font-size:22px;line-height:1.2;color:var(--blue)">Lorem ipsum dolor sit amet.</p>
  </section>

  <!-- 10 Timeline end -->
  <section class="slide">
    <div class="vline" style="top:0;bottom:80px"></div>
    <div class="vnode is-green" style="left:157px;top:32px"></div>
    <div class="vlabel to-left" style="left:42px;top:32px"><b>Infographic</b><span>Add a short note about this step here.</span></div>
    <div class="vnode is-grey" style="left:217px;top:74px"></div>
    <div class="vlabel" style="left:252px;top:74px"><b>Closing</b><span>Add a short note about this step here.</span></div>
    <p class="serif" style="position:absolute;left:150px;width:100px;top:140px;text-align:center;font-weight:500;font-size:14px;color:#333">Section End</p>
    <p style="position:absolute;left:140px;width:120px;top:158px;text-align:center;font-size:5.5px">A look at our presentation agenda</p>
    <div class="num">10</div>
  </section>

  <!-- 11 Photo slide -->
  <section class="slide">
    <div class="photo" role="img" aria-label="Photo of business people walking in a bright glass hall" style="inset:0;background:linear-gradient(120deg,#dfe9f3,#7f9bb8 55%,#f2f5f8)"></div>
    <div style="position:absolute;left:23px;top:41px;width:153px;height:148px;background:rgba(28,122,53,.82)"></div>
    <p class="serif" style="position:absolute;left:42px;top:50px;font-weight:700;font-size:31px;line-height:1.15;color:var(--white)">Your<br>Photo<br>Slide</p>
  </section>

  <!-- 12 Word -->
  <section class="slide">
    <div class="mark"><span class="ring"></span>Vantor Bellway</div>
    <p class="word" style="color:var(--blue)">Your Word<br>Here</p>
    <div class="num">12</div>
  </section>

  <!-- 13 Big number -->
  <section class="slide">
    <div class="mark"><span class="ring"></span>Vantor Bellway</div>
    <div style="position:absolute;left:0;width:260px;top:46px;text-align:center">
      <p class="big-number" style="font-size:66px">1500</p>
      <p class="big-caption" style="font-size:12px;margin-top:8px">Your Big Number Here</p>
    </div>
    <div class="num">13</div>
  </section>

  <!-- 14 Two numbers -->
  <section class="slide">
    <div class="mark"><span class="ring"></span>Vantor Bellway</div>
    <div style="position:absolute;left:8px;width:180px;top:60px;text-align:center">
      <p class="big-number" style="font-size:50px">1500</p>
      <p class="big-caption" style="font-size:10px;margin-top:8px">Your Big Number 1 Here</p>
    </div>
    <div style="position:absolute;left:192px;top:50px;width:1px;height:100px;background:#dcdcdc"></div>
    <div style="position:absolute;left:200px;width:180px;top:60px;text-align:center">
      <p class="big-number" style="font-size:50px">1500</p>
      <p class="big-caption" style="font-size:10px;margin-top:8px">Your Big Number 2 Here</p>
    </div>
    <div class="num">14</div>
  </section>

  <!-- 15 Word on blue -->
  <section class="slide fill-blue">
    <p class="word" style="color:var(--white)">Your Word<br>Here</p>
    <div class="num" style="color:rgba(255,255,255,.25)">15</div>
  </section>

  <!-- 16 Horizontal timeline -->
  <section class="slide">
    <h2 class="head">Our Timeline</h2>
    <div class="mark"><span class="ring"></span>Vantor Bellway</div>
    <div class="hline"></div>
    <div class="hlabel up" style="left:67px">Opening</div>
    <div class="hnode up is-green" style="left:67px"></div>
    <div class="hnode down is-blue" style="left:135px"></div>
    <div class="hlabel down" style="left:135px">Content 1</div>
    <div class="hlabel up" style="left:196px">Content 2</div>
    <div class="hnode up is-green" style="left:196px"></div>
    <div class="hnode down is-grey" style="left:261px"></div>
    <div class="hlabel down" style="left:261px">Content 3</div>
    <div class="hlabel up" style="left:327px">Content 4</div>
    <div class="hnode up is-green" style="left:327px"></div>
    <div class="num">16</div>
  </section>

  <!-- 17 -->
  <section class="slide">
    <h2 class="head">Our Timeline</h2>
    <div class="mark"><span class="ring"></span>Vantor Bellway</div>
    <div class="hline"></div>
    <div class="hnode down is-blue" style="left:60px"></div>
    <div class="hlabel down" style="left:60px">Content 5</div>
    <div class="hlabel up" style="left:123px">Content 6</div>
    <div class="hnode up is-green" style="left:123px"></div>
    <div class="hnode down is-grey" style="left:190px"></div>
    <div class="hlabel down" style="left:190px">Content 7</div>
    <div class="hlabel up" style="left:255px">Content 8</div>
    <div class="hnode up is-grey" style="left:255px"></div>
    <div class="hnode down is-green" style="left:320px"></div>
    <div class="hlabel down" style="left:320px">Content 9</div>
    <div class="num">17</div>
  </section>

  <!-- 18 -->
  <section class="slide">
    <h2 class="head">Our Timeline</h2>
    <div class="mark"><span class="ring"></span>Vantor Bellway</div>
    <div class="hline"></div>
    <div class="hnode up is-green" style="left:67px"></div>
    <div class="hnode down is-blue" style="left:130px"></div>
    <div class="hnode up is-grey" style="left:192px"></div>
    <div class="hnode down is-grey" style="left:255px"></div>
    <div class="hnode up is-green" style="left:318px"></div>
    <div class="num">18</div>
  </section>

  <!-- 19 Phrase blue -->
  <section class="slide fill-blue">
    <p class="phrase">Short Important<br>Phrase on Blue<br>Background</p>
    <div class="num" style="color:rgba(255,255,255,.25)">19</div>
  </section>

  <!-- 20 Phrase green -->
  <section class="slide fill-green">
    <p class="phrase" style="left:48px;top:38px">Short Important<br>Phrase on Blue<br><span style="padding-left:80px">Background</span></p>
    <div class="num" style="color:rgba(255,255,255,.25)">20</div>
  </section>

  <!-- 21 Word green -->
  <section class="slide fill-green">
    <p class="word" style="color:var(--white)">Your Word<br>Here</p>
    <div class="num" style="color:rgba(255,255,255,.25)">21</div>
  </section>

  <!-- 22 Two column bullets -->
  <section class="slide">
    <h2 class="head">Two Column Bullets list</h2>
    <div class="mark"><span class="ring"></span>Vantor Bellway</div>
    <ul class="bullets copy" style="position:absolute;left:18px;top:42px;width:168px">
      <li>Lorem ipsum dolor sit amet, consectetur adipiscing elit, sed do eiusmod tempor incididunt ut labore et dolore magna aliqua.</li>
      <li style="margin-top:14px">Duis aute irure dolor in reprehenderit in voluptate velit esse cillum dolore eu fugiat nulla pariatur excepteur sint.</li>
    </ul>
    <ul class="bullets copy" style="position:absolute;left:200px;top:42px;width:168px">
      <li>Lorem ipsum dolor sit amet, consectetur adipiscing elit, sed do eiusmod tempor incididunt ut labore et dolore magna aliqua.</li>
      <li style="margin-top:14px">Duis aute irure dolor in reprehenderit in voluptate velit esse cillum dolore eu fugiat nulla pariatur excepteur sint.</li>
    </ul>
    <div class="num">22</div>
  </section>

  <!-- 23 Three column -->
  <section class="slide">
    <h2 class="head">Three Column Area</h2>
    <div class="mark"><span class="ring"></span>Vantor Bellway</div>
    <div class="col-panel copy" style="left:14px;top:40px;width:114px;height:136px"><p>Lorem ipsum dolor sit amet, consectetur adipiscing elit, sed do eiusmod tempor incididunt ut labore et dolore magna aliqua.</p><p style="margin-top:10px">Duis aute irure dolor in reprehenderit in voluptate velit esse cillum dolore eu fugiat nulla pariatur excepteur sint.</p></div>
    <div class="col-panel copy" style="left:136px;top:40px;width:114px;height:136px"><p>Lorem ipsum dolor sit amet, consectetur adipiscing elit, sed do eiusmod tempor incididunt ut labore et dolore magna aliqua.</p><p style="margin-top:10px">Duis aute irure dolor in reprehenderit in voluptate velit esse cillum dolore eu fugiat nulla pariatur excepteur sint.</p></div>
    <div class="col-panel copy" style="left:258px;top:40px;width:114px;height:136px"><p>Lorem ipsum dolor sit amet, consectetur adipiscing elit, sed do eiusmod tempor incididunt ut labore et dolore magna aliqua.</p><p style="margin-top:10px">Duis aute irure dolor in reprehenderit in voluptate velit esse cillum dolore eu fugiat nulla pariatur excepteur sint.</p></div>
    <div class="num">23</div>
  </section>

  <!-- 24 One column list -->
  <section class="slide">
    <h2 class="head">One Column Big Unordered Lists</h2>
    <div class="mark"><span class="ring"></span>Vantor Bellway</div>
    <ul class="bullets" style="position:absolute;left:22px;top:50px;font-size:10.5px;line-height:21px;color:#555;white-space:nowrap">
      <li>Lorem ipsum dolor sit amet, consectetur adipiscing elit,</li>
      <li>Sed do eiusmod tempor incididunt ut labore et dolore magna</li>
      <li>Aliqua. Ut enim ad minim veniam, quis nostrud</li>
      <li>Exercitation ullamco laboris nisi ut aliquip ex ea commodo</li>
      <li>Sed do eiusmod tempor incididunt ut labore et dolore magna</li>
      <li>Aliqua. Ut enim ad minim veniam, quis nostrud</li>
      <li>Exercitation ullamco laboris nisi ut aliquip ex ea commodo</li>
    </ul>
    <div class="num">24</div>
  </section>

  <!-- 25 Photo + bullets -->
  <section class="slide">
    <h2 class="head">Your Photo Slide</h2>
    <div class="mark"><span class="ring"></span>Vantor Bellway</div>
    <div class="photo" role="img" aria-label="Photo of a modern glass building against the sky" style="left:0;right:0;top:44px;height:78px;background:linear-gradient(100deg,#6d89a8,#c9d6e3 55%,#f4e6d8)"></div>
    <ul class="bullets" style="position:absolute;left:16px;top:132px;font-size:10px;line-height:19px;color:#555;white-space:nowrap">
      <li>Lorem ipsum dolor sit amet, consectetur adipiscing elit,</li>
      <li>Sed do eiusmod tempor incididunt ut labore et dolore magna</li>
      <li>Aliqua. Ut enim ad minim veniam, quis nostrud</li>
    </ul>
    <div class="num">25</div>
  </section>

  <!-- 26 Two column area -->
  <section class="slide">
    <h2 class="head">Two Column Area</h2>
    <div class="mark"><span class="ring"></span>Vantor Bellway</div>
    <div class="col-panel copy" style="left:14px;top:38px;width:172px;height:148px"><p>Lorem ipsum dolor sit amet, consectetur adipiscing elit, sed do eiusmod tempor incididunt ut labore et dolore magna aliqua.</p><p style="margin-top:12px">Duis aute irure dolor in reprehenderit in voluptate velit esse cillum dolore eu fugiat nulla pariatur excepteur sint.</p></div>
    <div class="col-panel copy" style="left:196px;top:38px;width:172px;height:148px"><p>Lorem ipsum dolor sit amet, consectetur adipiscing elit, sed do eiusmod tempor incididunt ut labore et dolore magna aliqua.</p><p style="margin-top:12px">Duis aute irure dolor in reprehenderit in voluptate velit esse cillum dolore eu fugiat nulla pariatur excepteur sint.</p></div>
    <div class="num">26</div>
  </section>

  <!-- 27 World map -->
  <section class="slide">
    <h2 class="head">World Map</h2>
    <div class="mark"><span class="ring"></span>Vantor Bellway</div>
    <p class="serif" style="position:absolute;left:18px;top:70px;font-weight:700;font-size:13px;color:var(--green)">Fun Facts</p>
    <div style="position:absolute;left:18px;top:92px;font-size:9px;font-weight:600;color:var(--green)">55% <span style="color:#999;font-weight:400;font-size:6px">of people</span></div>
    <div style="position:absolute;left:18px;top:106px">
      <span class="person-ico is-green"></span><span class="person-ico is-green"></span><span class="person-ico is-green"></span><span class="person-ico is-green"></span><span class="person-ico is-green"></span><span class="person-ico is-grey"></span><span class="person-ico is-grey"></span><span class="person-ico is-grey"></span>
    </div>
    <div style="position:absolute;left:18px;top:126px;font-size:9px;font-weight:600;color:var(--blue)">45% <span style="color:#999;font-weight:400;font-size:6px">of people</span></div>
    <div style="position:absolute;left:18px;top:140px">
      <span class="person-ico is-blue"></span><span class="person-ico is-blue"></span><span class="person-ico is-blue"></span><span class="person-ico is-blue"></span><span class="person-ico is-grey"></span><span class="person-ico is-grey"></span><span class="person-ico is-grey"></span><span class="person-ico is-grey"></span>
    </div>
    <div role="img" aria-label="Dotted world map" style="position:absolute;left:118px;top:86px;width:258px;height:98px;border-radius:30px;background:radial-gradient(ellipse at center,#c9c9c9,rgba(201,201,201,.15) 70%,transparent)"></div>
    <div class="pin" style="left:163px;top:86px;color:var(--green)"><i class="is-green">55%</i></div>
    <div class="pin" style="left:184px;top:136px;color:var(--blue)"><i class="is-blue">17%</i></div>
    <div class="pin" style="left:232px;top:104px;color:#aab"><i class="is-grey">47%</i></div>
    <div class="pin" style="left:302px;top:94px;color:#aab"><i class="is-grey">5%</i></div>
    <div class="pin" style="left:332px;top:130px;color:var(--green)"><i class="is-green">33%</i></div>
  </section>

  <!-- 28 Time line wave -->
  <section class="slide">
    <h2 class="head">Time Line</h2>
    <div class="mark"><span class="ring"></span>Vantor Bellway</div>
    <p class="copy" style="position:absolute;left:18px;top:36px;width:330px">Lorem ipsum dolor sit amet, consectetur adipiscing elit, sed do eiusmod tempor incididunt ut labore et dolore magna aliqua.</p>
    <svg style="position:absolute;left:0;top:0" width="386" height="218" viewBox="0 0 386 218">
      <g fill="none" stroke-width="10">
        <path d="M34 122 A34 34 0 0 1 102 122" stroke="#22409a"/>
        <path d="M102 122 A34 34 0 0 0 170 122" stroke="#1c7a35"/>
        <path d="M170 122 A34 34 0 0 1 238 122" stroke="#22409a"/>
        <path d="M238 122 A34 34 0 0 0 306 122" stroke="#1c7a35"/>
        <path d="M306 122 A34 34 0 0 1 374 122" stroke="#22409a"/>
      </g>
      <g fill="#fff" stroke="#22409a" stroke-width="2">
        <circle cx="68" cy="122" r="6"/><circle cx="136" cy="122" r="6" stroke="#1c7a35"/><circle cx="204" cy="122" r="6"/><circle cx="272" cy="122" r="6" stroke="#1c7a35"/><circle cx="340" cy="122" r="6"/>
      </g>
      <g font-family="Open Sans, sans-serif" font-size="7" font-weight="600" text-anchor="middle" fill="#444">
        <text x="68" y="146">Date</text><text x="136" y="102">Date</text><text x="204" y="146">Date</text><text x="272" y="102">Date</text><text x="340" y="146">Date</text>
      </g>
      <g font-family="Open Sans, sans-serif" font-size="5" text-anchor="middle" fill="#777">
        <text x="68" y="155">Short note here</text><text x="136" y="93">Short note here</text><text x="204" y="155">Short note here</text><text x="272" y="93">Short note here</text><text x="340" y="155">Short note here</text>
      </g>
    </svg>
    <div class="num">28</div>
  </section>

  <!-- 29 Our team single -->
  <section class="slide">
    <h2 class="head">Our Team</h2>
    <div class="mark"><span class="ring"></span>Vantor Bellway</div>
    <div role="img" aria-label="Round portrait photo of a team member" style="position:absolute;left:148px;top:22px;width:90px;height:90px;border-radius:50%;background:linear-gradient(160deg,#c7b6a3,#6d6865)"></div>
    <p style="position:absolute;left:0;right:0;top:120px;text-align:center;font-size:7px;font-weight:600;color:#444">Mara Lind</p>
    <p style="position:absolute;left:0;right:0;top:130px;text-align:center;font-size:5.5px;color:var(--green)">CEO</p>
    <p style="position:absolute;left:118px;width:150px;top:142px;text-align:center;font-size:5.5px;line-height:1.4">A short line about this person and their role.</p>
    <div style="position:absolute;left:179px;top:162px;display:flex;gap:4px">
      <span style="width:7px;height:7px;border-radius:50%;background:var(--green)"></span><span style="width:7px;height:7px;border-radius:50%;background:var(--green)"></span><span style="width:7px;height:7px;border-radius:50%;background:var(--green)"></span>
    </div>
  </section>

  <!-- 30 Our team four -->
  <section class="slide">
    <h2 class="head">Our Team</h2>
    <div class="mark"><span class="ring"></span>Vantor Bellway</div>
    <div class="member" style="left:24px;top:56px"><div class="avatar" role="img" aria-label="Portrait photo of a team member"></div><div><b>Ivo Brandt</b><em>Director</em><span>Short note about work here.</span><span>Short note about work here.</span></div></div>
    <div class="member" style="left:194px;top:56px"><div class="avatar" role="img" aria-label="Portrait photo of a team member"></div><div><b>Tess Orlan</b><em>Manager</em><span>Short note about work here.</span><span>Short note about work here.</span></div></div>
    <div class="member" style="left:24px;top:128px"><div class="avatar" role="img" aria-label="Portrait photo of a team member" style="background:linear-gradient(160deg,#e3c9a3,#8c7a6a)"></div><div><b>Nadia Peel</b><em>Consultant</em><span>Short note about work here.</span><span>Short note about work here.</span></div></div>
    <div class="member" style="left:194px;top:128px"><div class="avatar" role="img" aria-label="Portrait photo of a team member"></div><div><b>Rui Castel</b><em>Analyst</em><span>Short note about work here.</span><span>Short note about work here.</span></div></div>
  </section>

  <!-- 31 Infographic rings -->
  <section class="slide">
    <h2 class="head">Visual Design Infographic</h2>
    <div class="mark"><span class="ring"></span>Vantor Bellway</div>
    <svg style="position:absolute;left:0;top:0" width="386" height="218" viewBox="0 0 386 218">
      <g fill="none" stroke-width="5">
        <path d="M64 92 A27 27 0 0 1 118 92" stroke="#22409a"/><path d="M64 92 A27 27 0 0 0 118 92" stroke="#1c7a35"/>
        <path d="M130 92 A27 27 0 0 1 184 92" stroke="#22409a"/><path d="M130 92 A27 27 0 0 0 184 92" stroke="#1c7a35"/>
        <path d="M196 92 A27 27 0 0 1 250 92" stroke="#22409a"/><path d="M196 92 A27 27 0 0 0 250 92" stroke="#1c7a35"/>
        <path d="M262 92 A27 27 0 0 1 316 92" stroke="#22409a"/><path d="M262 92 A27 27 0 0 0 316 92" stroke="#1c7a35"/>
      </g>
      <g fill="none" stroke="#22409a" stroke-width="1.5">
        <circle cx="91" cy="92" r="6"/><circle cx="157" cy="92" r="6"/><circle cx="223" cy="92" r="6"/><circle cx="289" cy="92" r="6"/>
      </g>
      <g font-family="Open Sans, sans-serif" text-anchor="middle" fill="#22409a">
        <g font-size="8" font-weight="600"><text x="91" y="140">01</text><text x="157" y="140">02</text><text x="223" y="140">03</text><text x="289" y="140">04</text></g>
        <g font-size="5.5" font-weight="600" fill="#444"><text x="91" y="152">BUSINESS</text><text x="157" y="152">MARKETING</text><text x="223" y="152">PRESENTATION</text><text x="289" y="152">SURVEY TEAM</text></g>
      </g>
    </svg>
    <div class="num">31</div>
  </section>

  <!-- 32 Infographic cards -->
  <section class="slide">
    <h2 class="head">Visual Design Infographic</h2>
    <div class="mark"><span class="ring"></span>Vantor Bellway</div>
    <div class="card" style="left:59px;border-color:var(--green)"><div class="tab is-green"></div><div class="lbl" style="border-color:var(--green);color:var(--green)">BUSINESS</div></div>
    <div class="card" style="left:125px"><div class="tab is-blue"></div><div class="lbl">BUSINESS</div></div>
    <div class="card" style="left:191px"><div class="tab is-blue"></div><div class="lbl">BUSINESS</div></div>
    <div class="card" style="left:257px"><div class="tab is-blue"></div><div class="lbl">BUSINESS</div></div>
    <div class="num">32</div>
  </section>

  <!-- 33 Thank you -->
  <section class="slide paper">
    <div style="position:absolute;left:40px;top:58px;display:flex;align-items:center;gap:8px;font-family:'Alegreya',serif;font-weight:700;font-size:24px;color:var(--green)">
      <span style="width:30px;height:30px;border-radius:50%;border:3px solid var(--green)"></span>Vantor Bellway
    </div>
    <div class="circuit" role="img" aria-label="Green and blue circuit-line decoration" style="left:0;bottom:0;width:263px;height:82px;background:linear-gradient(90deg,rgba(28,122,53,.35),rgba(34,64,154,.05))"></div>
    <p class="serif" style="position:absolute;right:16px;bottom:16px;font-weight:700;font-size:24px;color:var(--blue)">Thank you..</p>
  </section>

</main>
</body>
</html>
```